Luxury Caviar Tin Label for High End Caviar Retailer

We are looking for a new caviar label design. We want something unique, preferably black and gold or dark blue and gold. We want a modern and luxurious feel. We have several types of caviar so we need to be able to change the name of the caviar when we print the labels. See inspiration attached. Logo is also attached. More about us: kvmarlune.com

Industry/Entity Type

fine foods industry, caviar

Font styles to use
Serif
Decorative

Requirements
Must have
• KV Marlune Logo, space for caviar name
Nice to have
• black and gold, blue and gold

```html
<!DOCTYPE html>
<html lang="en">
<head>
<meta charset="utf-8">
<title>KV Marlune — Hackleback Caviar Tin Label</title>
<link rel="stylesheet" href="https://fonts.googleapis.com/css2?family=Cinzel:wght@400;500&family=Marcellus&family=Cormorant+Garamond:wght@500&display=swap">
<style>
  :root {
    --backdrop: #e7e7e7;
    --label-black: #030303;
    --pattern-black: #111111;
    --gold-light: #f3e7a4;
    --gold-mid: #d9b45a;
    --gold-deep: #8f6420;
    --gold-text: #c9983f;
  }
  html, body {
    margin: 0;
    padding: 0;
    width: 1186px;
    height: 1200px;
    overflow: hidden;
    background: var(--backdrop);
  }
  .tin-label {
    display: block;
    width: 1186px;
    height: 1200px;
  }
  .variety-name {
    font-family: "Cinzel", serif;
    font-size: 47px;
    letter-spacing: 4px;
  }
  .brand-name {
    font-family: "Marcellus", serif;
    font-size: 27px;
    letter-spacing: 1.5px;
  }
  .selection-line {
    font-family: "Cormorant Garamond", serif;
    font-weight: 500;
    font-size: 17px;
    letter-spacing: 0.5px;
  }
  .product-word {
    font-family: "Cinzel", serif;
    font-size: 58px;
    letter-spacing: 6px;
  }
  .care-line {
    font-family: "Cormorant Garamond", serif;
    font-weight: 500;
    font-size: 15.5px;
    letter-spacing: 0.6px;
  }
</style>
</head>
<body>
<svg class="tin-label" viewBox="0 0 1186 1200" xmlns="http://www.w3.org/2000/svg">
  <defs>
    <linearGradient id="gold-rim" x1="0" y1="0" x2="1" y2="1">
      <stop offset="0" stop-color="#c9b06a"/>
      <stop offset="0.35" stop-color="#f1e8a6"/>
      <stop offset="0.7" stop-color="#e6d692"/>
      <stop offset="1" stop-color="#a8956e"/>
    </linearGradient>
    <linearGradient id="gold-foil" x1="0" y1="0" x2="1" y2="0">
      <stop offset="0" stop-color="var(--gold-deep)"/>
      <stop offset="0.3" stop-color="var(--gold-mid)"/>
      <stop offset="0.5" stop-color="var(--gold-light)"/>
      <stop offset="0.7" stop-color="var(--gold-mid)"/>
      <stop offset="1" stop-color="var(--gold-deep)"/>
    </linearGradient>
    <linearGradient id="gold-type" x1="0" y1="0" x2="0" y2="1">
      <stop offset="0" stop-color="#f0d98c"/>
      <stop offset="0.55" stop-color="#c8913a"/>
      <stop offset="1" stop-color="#8a5c1c"/>
    </linearGradient>
    <radialGradient id="pattern-tone" cx="0.5" cy="0.5" r="0.5">
      <stop offset="0" stop-color="#151515"/>
      <stop offset="1" stop-color="#070707"/>
    </radialGradient>
    <path id="arc-top" d="M 326 596 A 267 267 0 0 1 860 596"/>
    <path id="arc-bottom" d="M 305 596 A 288 288 0 0 0 881 596"/>
  </defs>

  <!-- tin rim -->
  <circle cx="593" cy="596" r="419" fill="url(#gold-rim)"/>
  <circle cx="593" cy="596" r="388" fill="none" stroke="#9fae9a" stroke-width="4" opacity="0.6"/>

  <!-- label face -->
  <circle cx="593" cy="596" r="382" fill="var(--label-black)"/>

  <!-- dotted border band -->
  <g class="border-band" fill="none">
    <circle cx="593" cy="596" r="356" stroke="url(#gold-foil)" stroke-width="2.5"/>
    <circle cx="593" cy="596" r="345" stroke="url(#gold-foil)" stroke-width="5" stroke-dasharray="0 9.4" stroke-linecap="round"/>
    <circle cx="593" cy="596" r="334" stroke="url(#gold-foil)" stroke-width="2.5"/>
    <circle cx="593" cy="596" r="327" stroke="url(#gold-foil)" stroke-width="1.2"/>
  </g>

  <!-- side rules -->
  <g class="side-rules" fill="none" stroke="url(#gold-foil)" stroke-width="2.5">
    <path d="M 339 500 A 260 260 0 0 0 353 734"/>
    <path d="M 847 500 A 260 260 0 0 1 833 734"/>
  </g>

  <!-- inner medallion -->
  <circle cx="593" cy="596" r="238" fill="url(#pattern-tone)" role="img" aria-label="Faint dark swirling flourish pattern"/>
  <circle cx="593" cy="596" r="238" fill="none" stroke="url(#gold-foil)" stroke-width="1.5"/>
  <circle cx="593" cy="596" r="244" fill="none" stroke="url(#gold-foil)" stroke-width="0.8" opacity="0.7"/>

  <!-- variety name -->
  <text class="variety-name" fill="url(#gold-type)" text-anchor="middle">
    <textPath href="#arc-top" startOffset="50%">HACKLEBACK CAVIAR</textPath>
  </text>

  <!-- brand -->
  <text class="brand-name" x="593" y="565" fill="var(--gold-text)" text-anchor="middle">KV MARLUNE</text>

  <line x1="522" y1="616" x2="664" y2="616" stroke="url(#gold-foil)" stroke-width="2"/>

  <text class="selection-line" x="593" y="671" fill="var(--gold-text)" text-anchor="middle">EXCLUSIVE SELECTION</text>
  <text class="product-word" x="593" y="741" fill="url(#gold-type)" text-anchor="middle">CAVIAR</text>

  <!-- care and ingredients -->
  <text class="care-line" fill="var(--gold-text)" text-anchor="middle">
    <textPath href="#arc-bottom" startOffset="50%">Keep Refrigerated 28 - 34 | www.kvmarlune.com | Ingredients: caviar - salt</textPath>
  </text>
</svg>
</body>
</html>
```